Flyer Fewo Dorn
Trotz etlicher Änderungen immer Hilfsbereit und alle Wünsche wurden von Jonas 1A umgesetzt.
Sehr geehrte Damen und Herren, 01.12.25
wir werden jetzt gleich die Entscheidung treffen. Daher möchten wir uns bei Ihnen allen für die Entwürfe und gute Zusammenarbeit bedanken. Es war für uns recht schwierig den Gewinner festzulegen.
Mit freundlichen Grüßen
Familie Dorn
Sehr geehrte Damen und Herren,
Nachtrag. Bitte weisen Sie auf das:
1. Hügeltaler Kirschenfest vom 21.02.26 - 06.04.26
2. Oldimerveranstaltungen
3. Ausschrank Federweiser / neuer Wein ab September 2026
4. viele regionale Weinfeste
hin.
zunächst möchten wir uns bei Ihnen für die bisherigen Entwürfe bedanken. Wir haben eben die Textdatei überarbeitet und neu abgespeichert. Bitte überarbeiten Sie Ihre Texte in den Entwürfen. Sie können auch gerne textliche Passagen kürzer fassen.
Wir bitten Sie, die Weinregion südliche Weinstrasse etwas mehr im Hintergrund hervorzuheben.
Wir melden uns wenn dann nach der Überarbeitung der Texte.
Mit freundlichem Gruß
Aufgabenstellung
Warmes Design, bezogen auf die Weinregion, hoher Freizeitwert, zentral gelegen. Bodenständig, da die Wohnung in einem Haus ausgebaut ist was keinerlei Grautöne hat. Das 2 Familienhaus ist im italienischen Stil gebaut

```html
<!DOCTYPE html>
<html lang="de">
<head>
<meta charset="utf-8">
<title>Fewo Dorn – Ausstattung</title>
<link rel="stylesheet" href="https://fonts.googleapis.com/css2?family=Open+Sans:wght@400;600;700&display=swap">
<style>
  :root {
    --wine: #731f18;
    --paper: #ffffff;
    --text-light: #fbeeea;
  }
  * { margin: 0; padding: 0; box-sizing: border-box; }
  html, body { width: 855px; height: 1200px; overflow: hidden; }
  body {
    background: var(--wine);
    font-family: "Open Sans", Arial, sans-serif;
    color: var(--text-light);
  }
  .flyer { position: relative; width: 855px; height: 1200px; }

  .features { position: absolute; left: 65px; top: 58px; width: 740px; }
  .section-title {
    font-weight: 700; font-size: 21px; letter-spacing: 0.5px;
    color: var(--paper); margin-bottom: 16px;
  }
  .features p {
    font-size: 16.3px; line-height: 19.4px; margin-bottom: 19.4px;
  }

  .included {
    position: absolute; left: 40px; top: 592px; right: 0; height: 337px;
    background: var(--paper); color: var(--wine);
    padding: 12px 0 0 22px;
  }
  .included .section-title { color: var(--wine); margin-bottom: 14px; font-size: 21px; }
  .included-columns { display: flex; }
  .included-list { list-style: none; font-weight: 600; font-size: 16px; line-height: 21.6px; }
  .included-list.left { width: 373px; }
  .included-list.right { width: 360px; }
  .included-list li { position: relative; padding-left: 16px; }
  .included-list li::before { content: "•"; position: absolute; left: 0; }

  .detail { position: absolute; left: 62px; width: 740px; }
  .detail-title {
    font-weight: 700; font-size: 17.5px; text-decoration: underline;
    text-underline-offset: 3px; color: var(--paper); margin-bottom: 18px;
  }
  .detail p { font-size: 16.3px; line-height: 19.4px; }
  .beds { top: 949px; }
  .sanitary { top: 1047px; }
</style>
</head>
<body>
<main class="flyer">
  <section class="features">
    <h2 class="section-title">AUSSTATTUNGEN</h2>
    <p>Die lichtdurchflutete Wohnung hat einen eigenen, separaten Haus- und<br>Wohnungseingang. Ein PKW-Stellplatz ist auf dem Grundstück vorhanden.<br>E-Bikes/Fahrräder können Sie in unserer Garage sicher abstellen. Die Wohnung hat ca.<br>76 qm mit einem großzügigen Wohn-Esszimmer. In diesem befindet sich auch eine<br>Schlafcouch für zwei weitere Gäste.</p>
    <p>Die neue Einbauküche ist mit allen E-Geräten ausgestattet, und an der großen<br>Kücheninsel können Sie gemeinsam kochen oder gemütlich speisen. Im Schlafzimmer<br>erwartet Sie ein großes, bequemes Boxspringbett sowie ein 3 m großer Kleiderschrank<br>mit TV-Gerät. Das schöne Bad verfügt über eine Badewanne und eine Dusche mit<br>Sitzbank.</p>
    <p>Ein separates Gäste-WC steht Ihnen im Erdgeschoss frei zugänglich im Treppenhaus zur<br>Verfügung. Eine kleine Abstellkammer mit Waschmaschine, Bügelbrett, Bügeleisen sowie<br>einem mobilen Wäscheständer ist vorhanden. Weiterhin besitzt die Wohnung zwei<br>überdachte Balkone. Auf dem 12 qm großen Balkon können Sie entspannen und die<br>Sonne genießen. Von dem kleinen Balkon genießt man die schönen Sonnenuntergänge<br>mit Blick auf die Haardt. So können Sie Ihre Abende bei einem Glas Wein erholsam<br>ausklingen lassen. Alles wurde im Jahr 2024/25 fertiggestellt, in einem kleinen<br>Wohngebiet aus dem Jahr 2016, ganz nah an den Weinreben.</p>
    <p>Nichtraucherwohnung/Haus – Rauchen ist ausschließlich auf den beiden Balkonen<br>erlaubt. Keine Unterkunft für Kinder, Kleinkinder oder Enkelkinder. Nicht für Partygäste<br>geeignet.</p>
  </section>

  <section class="included">
    <h2 class="section-title">INKLUSIVE</h2>
    <div class="included-columns">
      <ul class="included-list left">
        <li>Kostenloses WLAN<br>(Nutzung auf eigene Gefahr)</li>
        <li>eigene Waschmaschine</li>
        <li>Wäscheständer zum trocken</li>
        <li>Handtücher</li>
        <li>Bettwäsche</li>
        <li>Seife</li>
        <li>Toilettenpapier</li>
        <li>Haarföhn</li>
        <li>Mülltrennung</li>
        <li>Haustiere nach vorheriger Rücksprache<br>gestattet. Max. 1 Hund</li>
      </ul>
      <ul class="included-list right">
        <li>Fußbodenheizung</li>
        <li>Vollständig ausgestattete<br>Hollmer-Einbauküche mit Kochinsel sowie<br>Geschirr, Töpfen und Pfannen für 4<br>Personen</li>
        <li>Kaffeevollautomat</li>
        <li>Wendorf Wohnwand mit 55 Zoll LED TV</li>
        <li>Privater eigener Eingang</li>
        <li>Rauchmelder</li>
        <li>LED Beleuchtung</li>
      </ul>
    </div>
  </section>

  <section class="detail beds">
    <h3 class="detail-title">BETTENVERTEILUNG</h3>
    <p>Anzahl Doppelbett: 1 (Boxspringbett) + im Wohnzimmer eine ausziehbare<br>Doppelschlafcouch</p>
  </section>

  <section class="detail sanitary">
    <h3 class="detail-title">SANITÄRE AUSSTATTUNG</h3>
    <p>Badewanne, Badezimmer Anzahl: 1, 1 × Dusche, Sitzbank in der Dusche, separates<br>Gäste-WC im Treppenhaus im EG</p>
  </section>
</main>
</body>
</html>
```